KPU Stationary
Business cards, envelopes and letterhead
Professional
Tom Vashel
Director
482 Brindle Crt
Willingboro, NJ 08046
T_Vashel@kp-union.com
www.KP-Union.com

```html
<!DOCTYPE html>
<html lang="en">
<head>
<meta charset="utf-8">
<title>KPU Stationery</title>
<link href="https://fonts.googleapis.com/css2?family=Roboto:wght@400;700&display=swap" rel="stylesheet">
<style>
:root{
  --bg:#e6e6e8;
  --paper:#ffffff;
  --navy:#0b1a5e;
  --blue:#1f35b8;
  --sky:#6f86e6;
  --ink:#333a4a;
  --muted:#7a8090;
}
*{margin:0;padding:0;box-sizing:border-box}
html,body{width:1200px;height:866px;overflow:hidden}
body{background:var(--bg);font-family:"Roboto",Arial,sans-serif;color:var(--ink);position:relative}
.sheet{position:absolute;background:var(--paper);box-shadow:0 3px 10px rgba(0,0,0,.18);overflow:hidden}
.brand{display:flex;align-items:center;gap:8px}
.brand-dot{width:30px;height:30px;border-radius:50%;background:var(--blue);flex:none}
.brand-name{font-weight:700;color:var(--navy);line-height:1}
.brand-name .big{display:block;font-size:22px}
.brand-name .small{display:block;font-size:7px;letter-spacing:.5px;margin-top:2px}
.swoosh{position:absolute;left:0;bottom:0;width:100%}
.tagline{position:absolute;bottom:8px;left:0;width:100%;text-align:center;font-size:6px;font-weight:700;letter-spacing:.6px;color:#fff}

/* letterhead */
.letterhead{left:40px;top:60px;width:460px;height:650px}
.letterhead .brand{position:absolute;left:30px;top:34px}
.contact{position:absolute;left:205px;top:34px;border-left:1px solid #c8cbd6;padding-left:10px;font-size:6.5px;line-height:1.5;color:var(--muted)}
.letter-body{position:absolute;left:30px;top:120px;width:400px;font-size:7px;line-height:1.55}
.letter-body p{margin-bottom:9px}
.recipient{margin-bottom:12px}
.subject b{margin-right:18px}
.signature{width:70px;height:20px;margin:6px 0 4px;background:linear-gradient(90deg,#8da0e8,#2d44c0);border-radius:3px;opacity:.7}

/* cards */
.card{width:290px;height:166px;top:60px}
.card-front{left:540px}
.card-front .brand{position:absolute;left:20px;top:22px}
.card-person{position:absolute;right:22px;top:76px;font-size:7px;line-height:1.5;text-align:left;width:120px}
.card-person strong{font-size:10px;color:var(--navy)}
.card-back{left:870px;background:radial-gradient(ellipse at 50% 40%,var(--blue),var(--navy) 80%)}
.card-back .brand{position:absolute;left:50%;top:50%;transform:translate(-50%,-50%)}
.card-back .brand-dot{background:#fff}
.card-back .brand-name{color:#fff}

/* envelopes */
.envelope{left:540px;width:620px;height:260px}
.envelope-back{top:250px}
.envelope-back svg{position:absolute;left:0;top:0;width:100%;height:100%}
.envelope-front{top:534px}
.envelope-front .brand{position:absolute;left:24px;top:22px}
.envelope-front .address{position:absolute;left:24px;top:64px;font-size:6.5px;line-height:1.5;color:var(--muted)}
</style>
</head>
<body>

<svg width="0" height="0" style="position:absolute">
  <defs>
    <linearGradient id="band" x1="0" x2="1" y1="0" y2="0">
      <stop offset="0" stop-color="#0b1a5e"/>
      <stop offset=".55" stop-color="#1f35b8"/>
      <stop offset="1" stop-color="#0b1a5e"/>
    </linearGradient>
  </defs>
</svg>

<section class="sheet letterhead">
  <div class="brand">
    <span class="brand-dot"></span>
    <span class="brand-name"><span class="big">KPU</span><span class="small">KESTREL PARTS UNION</span></span>
  </div>
  <div class="contact">
    482 Brindle Crt<br>Willingboro, NJ 08046<br>Phone: (609) 555-0142<br>Fax: (609) 555-0143<br>T_Vashel@kp-union.com<br>www.KP-Union.com
  </div>
  <div class="letter-body">
    <p>Date Here</p>
    <p class="recipient">Name Surname<br>Company Name<br>State Town Block B<br>Suite 1234<br>NY ABC01 2345</p>
    <p class="subject"><b>Subject</b> <b>Subject Goes Here</b></p>
    <p>Dear Surname,</p>
    <p>Thank you for your continued partnership with our team. This letter confirms the details we discussed last week regarding supply schedules, pricing for the coming quarter and the new ordering portal that will open to all members next month.</p>
    <p>Our regional staff will contact you to arrange a short review of current stock levels and delivery routes. Please keep your account details ready so we can complete the update quickly.</p>
    <p>Should you have any questions, our office is open weekdays and we will gladly help.</p>
    <p>Sincerely,</p>
    <div class="signature" role="img" aria-label="Handwritten signature"></div>
    <p>Name Surname<br>Your Title</p>
  </div>
  <svg class="swoosh" viewBox="0 0 460 70" preserveAspectRatio="none" height="70">
    <path d="M0,22 C140,62 300,-4 460,18" fill="none" stroke="var(--sky)" stroke-width="1.5"/>
    <path d="M0,30 C150,72 300,8 460,26 L460,70 L0,70Z" fill="url(#band)"/>
  </svg>
  <div class="tagline">"RELIABLE PARTS FOR EVERY PARTNER"</div>
</section>

<section class="sheet card card-front">
  <div class="brand">
    <span class="brand-dot"></span>
    <span class="brand-name"><span class="big">KPU</span><span class="small">KESTREL PARTS UNION</span></span>
  </div>
  <div class="card-person">
    <strong>Tom Vashel</strong><br>Director<br><br>482 Brindle Crt<br>Willingboro, NJ 08046<br>T_Vashel@kp-union.com<br>www.KP-Union.com
  </div>
</section>

<section class="sheet card card-back">
  <div class="brand">
    <span class="brand-dot"></span>
    <span class="brand-name"><span class="big">KPU</span><span class="small">KESTREL PARTS UNION</span></span>
  </div>
</section>

<section class="sheet envelope envelope-back">
  <svg viewBox="0 0 620 260" preserveAspectRatio="none">
    <path d="M0,0 L620,0 L620,40 C450,150 170,150 0,40Z" fill="url(#band)"/>
    <path d="M0,48 C170,160 450,160 620,48" fill="none" stroke="var(--sky)" stroke-width="2"/>
  </svg>
</section>

<section class="sheet envelope envelope-front">
  <div class="brand">
    <span class="brand-dot"></span>
    <span class="brand-name"><span class="big">KPU</span><span class="small">KESTREL PARTS UNION</span></span>
  </div>
  <div class="address">482 Brindle Crt<br>Willingboro, NJ 08046<br>www.KP-Union.com</div>
  <svg class="swoosh" viewBox="0 0 620 70" preserveAspectRatio="none" height="70">
    <path d="M0,22 C190,62 400,-4 620,18" fill="none" stroke="var(--sky)" stroke-width="1.5"/>
    <path d="M0,30 C200,72 400,8 620,26 L620,70 L0,70Z" fill="url(#band)"/>
  </svg>
  <div class="tagline">"RELIABLE PARTS FOR EVERY PARTNER"</div>
</section>

</body>
</html>
```